Wholistic Health Clinic (Chiropractic Osteopathic Naturapathic Homeopathic New Website Design

Create a beautiful website for Fenwick Chiropractic clinic that has been in the Sutherland Shire for over 40 years, that exemplifies the passion for helping people with their health goals using that may include a variety of techniques including Chiropractic, Osteopathy, Acupuncture, Applied Kinesiology, Retained Neonatal Reflexes, Nutritional Advice, Exercise Prescription, Decompression therapy, Massage and Stress management techniques.
We have a wholistic approach that includes Nutritional, Emotional and Physical health

(A more detailed draft will be supplied shortly)

Pages:
Home page
About Us Page
Team Page
Contact page
Terms of service Page
Privacy Page
and any other relevant page(s)

Will supply photos for:
- The Team Page and their qualifications & brief resume
- About Us page

Will supply logos for:
BPN
TORVEX
PLORIVEN
GRANTLEAF
MVA
KPO

Target Market(s)

main target Parents of young children and those 20's to 60's who live in the Sutherland Shire & have disposable income (that said almost everybody would benefit from their services)

Coding

Coded - Design and coding required

Number of Pages Required

5+ page

Font styles to use
Sans Serif

Requirements
Must have
• Please follow the brief

1. Easy to manage ourselves to add alerts (like Covid 19 compliance & Harbel week etc.) & update content like photos of team members etc.
2. Must be responsive and look good on mobile devices
3. must be fast loading
4. Logo on every page
5. Easy navigation on every page
6. Phone number must be clickable
7. Terms of service & Privacy pages
8. Slider on page 1 using photo of healthy people of all ages enjoying various lifestyles & ability to add other photos easily
Should not have
• no testimonials or any non compliant elements according to the BPN

```html
<!DOCTYPE html>
<html lang="en">
<head>
<meta charset="utf-8">
<title>Fenwick Chiropractic</title>
<link href="https://fonts.googleapis.com/css2?family=Lato:wght@400;700;900&family=Open+Sans:wght@400;600;700&display=swap" rel="stylesheet">
<style>
:root{
  --orange:#f26b3a;
  --ink:#2b2b2b;
  --text:#555;
  --muted:#888;
  --grey-bg:#f1f1f1;
  --dark:#1b1b1b;
  --white:#fff;
}
*{box-sizing:border-box;margin:0;padding:0}
html,body{width:1200px;height:2544px;overflow:hidden;background:var(--white)}
body{position:relative;font-family:"Open Sans",Arial,sans-serif;color:var(--text)}
.abs{position:absolute}

/* header + hero */
.hero{left:0;top:0;width:1200px;height:560px;background:linear-gradient(180deg,#9ec3de 0%,#c9dcea 40%,#e6d7bf 72%,#d9c3a0 100%)}
.site-header{left:0;top:0;width:1200px;height:70px;display:flex;align-items:center;padding:0 40px;background:rgba(255,255,255,.15)}
.brand{display:flex;align-items:center;gap:10px;font-family:"Lato",sans-serif;font-weight:700;font-size:17px;color:var(--white)}
.brand-mark{width:28px;height:28px;border-radius:50%;background:var(--white)}
.main-nav{display:flex;gap:28px;margin-left:auto;margin-right:48px;font-family:"Lato",sans-serif;font-size:13px;font-weight:700;color:var(--white)}
.main-nav .active{color:var(--orange);border-bottom:2px solid var(--orange);padding-bottom:3px}
.header-phone{display:flex;align-items:center;gap:8px;font-family:"Lato",sans-serif;font-weight:700;font-size:22px;color:var(--white)}
.hero-caption{left:360px;top:300px;width:480px;text-align:center;background:rgba(255,255,255,.82);padding:10px 10px 12px}
.hero-caption p{font-family:"Lato",sans-serif;font-size:19px;color:var(--ink);line-height:1.3}
.hero-caption strong{display:block;font-family:"Lato",sans-serif;font-weight:900;font-size:19px;color:var(--ink);letter-spacing:.2px;white-space:nowrap;line-height:1.35}
.hero-btn{left:510px;top:384px;width:180px;height:30px;background:var(--orange);color:var(--white);font-family:"Lato",sans-serif;font-weight:700;font-size:12px;display:flex;align-items:center;justify-content:center;letter-spacing:.4px}
.slider-arrow{top:336px;width:34px;height:34px;border-radius:50%;background:rgba(255,255,255,.85);display:flex;align-items:center;justify-content:center}

/* content sections */
.section-title{font-family:"Lato",sans-serif;font-weight:400;font-size:38px;color:var(--orange);letter-spacing:.5px;line-height:1}
.section-copy p{font-size:15px;line-height:1.75;color:var(--text);margin-bottom:26px}
.read-more{width:120px;height:34px;background:var(--orange);color:var(--white);font-family:"Lato",sans-serif;font-weight:700;font-size:12px;display:flex;align-items:center;justify-content:center;letter-spacing:.4px}
.grey-band{left:0;top:1180px;width:1200px;height:520px;background:var(--grey-bg)}

/* info bar + footer */
.info-bar{left:0;top:2380px;width:1200px;height:78px;background:#e9e9e9;display:flex;justify-content:center;gap:24px;align-items:center}
.info-box{width:380px;height:56px;background:#f7f7f7;display:flex;align-items:center;gap:14px;padding:0 16px}
.info-icon{width:34px;height:34px;border-radius:50%;background:var(--orange);display:flex;align-items:center;justify-content:center;flex:none}
.info-box p{font-size:12px;line-height:1.45;color:var(--ink);font-weight:600}
.site-footer{left:0;top:2458px;width:1200px;height:86px;background:var(--dark);padding:20px 40px;display:flex;align-items:center}
.footer-links{font-size:12px;color:#bbb;line-height:2}
.footer-links span{margin-right:14px}
.footer-legal{font-size:11px;color:#888}
.signup{margin-left:auto;display:flex;align-items:center;gap:18px}
.signup-field{width:200px;height:32px;background:var(--white);display:flex;align-items:center;padding-left:10px;font-size:11px;color:var(--muted);position:relative}
.signup-go{position:absolute;right:0;top:0;width:32px;height:32px;background:var(--orange)}
.social{width:22px;height:22px;border-radius:50%;background:#777}
</style>
</head>
<body>

<div class="abs hero" role="img" aria-label="Slider photo of a happy group of friends jumping together on a sunny beach"></div>

<header class="abs site-header">
  <div class="brand"><span class="brand-mark"></span>Fenwick Chiropractic</div>
  <nav class="main-nav">
    <span class="active">HOME</span><span>SERVICES</span><span>ABOUT US</span><span>TEAM</span><span>CONTACT US</span>
  </nav>
  <div class="header-phone">
    <svg width="20" height="20" viewBox="0 0 24 24"><path fill="#fff" d="M6.6 10.8a15 15 0 0 0 6.6 6.6l2.2-2.2c.3-.3.7-.4 1-.2 1.1.4 2.3.6 3.6.6.6 0 1 .4 1 1V20c0 .6-.4 1-1 1A17 17 0 0 1 3 4c0-.6.4-1 1-1h3.5c.6 0 1 .4 1 1 0 1.3.2 2.5.6 3.6.1.3 0 .7-.2 1z"/></svg>
    (02) 9000 4123
  </div>
</header>

<div class="abs hero-caption">
  <p>We have a holistic approach that includes</p>
  <strong>NUTRITIONAL, EMOTIONAL &amp; PHYSICAL HEALTH</strong>
</div>
<div class="abs hero-btn">BOOK AN APPOINTMENT</div>
<div class="abs slider-arrow" style="left:36px"><svg width="14" height="14" viewBox="0 0 14 14"><path d="M9 2 4 7l5 5" stroke="#333" stroke-width="2" fill="none"/></svg></div>
<div class="abs slider-arrow" style="left:1130px"><svg width="14" height="14" viewBox="0 0 14 14"><path d="M5 2l5 5-5 5" stroke="#333" stroke-width="2" fill="none"/></svg></div>

<svg class="abs" style="left:0;top:500px" width="1200" height="110" viewBox="0 0 1200 110">
  <path d="M0 30 C250 90 450 0 700 36 S1050 80 1200 20 L1200 110 L0 110Z" fill="#1b1b1b"/>
  <path d="M0 46 C250 104 450 16 700 52 S1050 94 1200 38 L1200 110 L0 110Z" fill="#fff"/>
</svg>

<!-- Who we are -->
<h2 class="abs section-title" style="left:144px;top:752px">WHO WE ARE</h2>
<div class="abs section-copy" style="left:144px;top:810px;width:560px">
  <p>Fenwick Chiropractic, situated in Marlow Point and established for over 40 years, is passionate about helping you achieve your health care goals. We use a unique approach, understand you are an individual, and tailor your treatment accordingly.</p>
  <p>We understand your musculoskeletal health may be affected by structural, biochemical or emotional factors and address these issues in your tailored treatment plan.</p>
</div>
<div class="abs read-more" style="left:144px;top:1076px">READ MORE</div>
<div class="abs" style="left:780px;top:752px;width:392px;height:360px;background:radial-gradient(circle at 50% 55%,#e2673d 0%,#c99a86 25%,#cfc9c6 55%,#e4e2e1 100%)" role="img" aria-label="Photo of a person's bare back with the spine highlighted in orange"></div>

<!-- What we do -->
<svg class="abs" style="left:0;top:1140px" width="1200" height="42" viewBox="0 0 1200 42">
  <path d="M0 40 C300 0 800 0 1200 40 L1200 42 L0 42Z" fill="#f1f1f1"/>
</svg>
<div class="abs grey-band"></div>
<h2 class="abs section-title" style="left:640px;top:1252px">WHAT WE DO</h2>
<div class="abs section-copy" style="left:640px;top:1306px;width:520px">
  <p>We use many Chiropractic techniques in our clinic to help patients manage a range of musculoskeletal conditions and these are modified to all ages, from the newborn to the elderly, for a better quality of life.</p>
  <p>Chiropractors are spinal experts, so when it comes to back pain, sciatica, neck pain, headaches from the neck and jaw, whiplash injuries or migraines we can be of assistance.</p>
</div>
<div class="abs read-more" style="left:640px;top:1560px">READ MORE</div>
<div class="abs" style="left:144px;top:1272px;width:384px;height:368px;background:radial-gradient(circle at 60% 50%,#e46a3c 0%,#3c6f9c 35%,#163a66 70%,#0d2545 100%)" role="img" aria-label="Illustration of a human skeleton with the spine glowing in orange on a blue background"></div>

<svg class="abs" style="left:0;top:1690px" width="1200" height="110" viewBox="0 0 1200 110">
  <path d="M0 0 L1200 0 L1200 40 C900 100 600 20 300 60 C180 75 80 70 0 55Z" fill="#f1f1f1"/>
  <path d="M0 55 C80 70 180 75 300 60 C600 20 900 100 1200 40 L1200 70 C900 130 600 50 300 85 C180 100 80 95 0 80Z" fill="#1b1b1b"/>
</svg>

<!-- What to expect -->
<h2 class="abs section-title" style="left:144px;top:1880px">WHAT TO EXPECT</h2>
<div class="abs section-copy" style="left:144px;top:1936px;width:560px">
  <p>If you've never had Chiropractic before, don't worry. We will explain everything as we go and answer any of your questions as you have them.</p>
  <p>On your first visit we will talk about your health history, complete a physical examination which usually involves asking you to do some movements, or simple tests and then finding the affected area to determine the cause of your problem. Once the problem has been identified we will discuss if you need any further tests...</p>
</div>
<div class="abs read-more" style="left:144px;top:2250px">READ MORE</div>
<div class="abs" style="left:780px;top:1900px;width:392px;height:400px;background:linear-gradient(160deg,#f3f3f3 0%,#dcd6cf 50%,#c9b8a6 100%)" role="img" aria-label="Photo of a chiropractor adjusting a seated patient's neck"></div>

<!-- Info bar -->
<div class="abs info-bar">
  <div class="info-box">
    <span class="info-icon"><svg width="18" height="18" viewBox="0 0 24 24"><circle cx="12" cy="12" r="9" stroke="#fff" stroke-width="2" fill="none"/><path d="M12 7v5l3 2" stroke="#fff" stroke-width="2" fill="none"/></svg></span>
    <p>MONDAY to FRIDAY: 9am - 5.30pm<br>SAT: 9am - 1pm</p>
  </div>
  <div class="info-box">
    <span class="info-icon"><svg width="16" height="16" viewBox="0 0 24 24"><path fill="#fff" d="M6.6 10.8a15 15 0 0 0 6.6 6.6l2.2-2.2c.3-.3.7-.4 1-.2 1.1.4 2.3.6 3.6.6.6 0 1 .4 1 1V20c0 .6-.4 1-1 1A17 17 0 0 1 3 4c0-.6.4-1 1-1h3.5c.6 0 1 .4 1 1 0 1.3.2 2.5.6 3.6.1.3 0 .7-.2 1z"/></svg></span>
    <p>Clinic hours may vary, please call us.<br>02 9000 4123 &nbsp;|&nbsp; 0400 555 019</p>
  </div>
</div>

<!-- Footer -->
<footer class="abs site-footer">
  <div>
    <div class="footer-links"><span>Home</span><span>Services</span><span>Testimonials</span><span>About Us</span><span>Team</span><span>Contact Us</span></div>
    <div class="footer-legal">Copyright © 2020 - Fenwick Chiropractic - All rights reserved &nbsp;·&nbsp; Terms of service &nbsp;·&nbsp; Privacy Policy</div>
  </div>
  <div class="signup">
    <div class="signup-field">Enter Email Address<span class="signup-go"></span></div>
    <span class="social"></span><span class="social"></span>
  </div>
</footer>

</body>
</html>
```